Commercial Business Card - stand out, clean, simple, unique.

commercial real estate group located in Texas. Called 4 Ridges Real Estate. We want a unique yet clean and professional card. On one side I would like the 4R to be by itself or to look as unique or tasteful as possible. We have the logo in white, black, and color in case a black background or something similar looks best on one side. We need a space for our name, email, cell. website. And possibly room for a phrase or city.

Contact Information for Business Card

Name, Title, Email, Phone Number, website

```html
<!DOCTYPE html>
<html lang="en">
<head>
<meta charset="utf-8">
<title>4 Ridges Real Estate — Business Card</title>
<link rel="stylesheet" href="https://fonts.googleapis.com/css2?family=Open+Sans:wght@400;600&display=swap">
<style>
  :root {
    --backdrop: #23272e;
    --card-white: #ffffff;
    --card-black: #050507;
    --edge-blue: #1f3fd6;
    --navy: #1c2a8c;
    --orange: #e0672a;
    --ink: #1a1a1a;
    --soft-white: #f2f2f2;
  }
  * { margin: 0; padding: 0; box-sizing: border-box; }
  html, body { width: 1200px; height: 1200px; overflow: hidden; }
  body {
    background: var(--backdrop);
    font-family: "Open Sans", Arial, sans-serif;
    position: relative;
  }
  .card {
    position: absolute;
    left: 180px;
    width: 840px;
    height: 480px;
    border-bottom: 8px solid var(--edge-blue);
    box-shadow: 0 18px 40px rgba(0,0,0,0.45);
  }
  .card-front { top: 90px; background: var(--card-white); }
  .card-back  { top: 630px; background: var(--card-black); }

  /* Front */
  .brand {
    position: absolute;
    left: 60px;
    top: 62px;
    display: flex;
    align-items: center;
    gap: 16px;
  }
  .brand-mark {
    width: 22px; height: 22px;
    background: var(--navy);
  }
  .brand-name {
    font-weight: 600;
    font-size: 34px;
    letter-spacing: 1px;
    color: var(--navy);
  }
  .person {
    position: absolute;
    right: 60px;
    top: 62px;
    text-align: right;
  }
  .person-name { font-size: 30px; color: var(--orange); letter-spacing: 1px; }
  .person-title { font-size: 26px; color: var(--ink); margin-top: 4px; }
  .divider {
    position: absolute;
    left: 60px; right: 160px;
    top: 178px;
    height: 2px;
    background: var(--orange);
  }
  .contact {
    position: absolute;
    left: 60px;
    top: 212px;
    font-size: 19px;
    color: var(--ink);
    line-height: 1.55;
  }
  .address { margin-bottom: 10px; }
  .contact-row { display: flex; align-items: center; gap: 14px; }
  .contact-row svg { width: 20px; height: 20px; flex: none; }

  /* Back */
  .back-brand {
    position: absolute;
    left: 0; right: 0;
    top: 170px;
    display: flex;
    justify-content: center;
    align-items: center;
    gap: 18px;
  }
  .back-brand .brand-mark { background: var(--edge-blue); width: 26px; height: 26px; }
  .back-brand .brand-name { color: var(--edge-blue); font-size: 42px; }
  .tagline {
    position: absolute;
    left: 0; right: 0;
    top: 300px;
    display: flex;
    justify-content: center;
    align-items: center;
    gap: 18px;
    color: var(--soft-white);
    font-size: 22px;
  }
  .tagline-rule { width: 90px; height: 1px; background: #7a6a66; }
</style>
</head>
<body>
  <section class="card card-front">
    <div class="brand">
      <span class="brand-mark"></span>
      <span class="brand-name">4 Ridges Real Estate</span>
    </div>
    <div class="person">
      <div class="person-name">Mark Hollander</div>
      <div class="person-title">CEO</div>
    </div>
    <div class="divider"></div>
    <div class="contact">
      <div class="address">#210 - 4870 Ridgeline Avenue<br>Austin, TX 78701</div>
      <div class="contact-row">
        <svg viewBox="0 0 20 20" aria-hidden="true"><path d="M5 2h4l1 5-2.5 1.5a10 10 0 0 0 4 4L13 10l5 1v4a2 2 0 0 1-2 2A14 14 0 0 1 3 4a2 2 0 0 1 2-2z" fill="var(--navy)"/></svg>
        <span>512.555.0148</span>
      </div>
      <div class="contact-row">
        <svg viewBox="0 0 20 20" aria-hidden="true"><rect x="2" y="4" width="16" height="12" rx="1" fill="var(--navy)"/><path d="M2 5l8 6 8-6" stroke="#fff" stroke-width="1.5" fill="none"/></svg>
        <span>hello@ridgesco.com</span>
      </div>
      <div class="contact-row">
        <svg viewBox="0 0 20 20" aria-hidden="true"><circle cx="10" cy="10" r="8" fill="none" stroke="var(--navy)" stroke-width="1.6"/><ellipse cx="10" cy="10" rx="3.5" ry="8" fill="none" stroke="var(--navy)" stroke-width="1.4"/><path d="M2 10h16M3.5 6h13M3.5 14h13" stroke="var(--navy)" stroke-width="1.2"/></svg>
        <span>www.ridgesco.com</span>
      </div>
    </div>
  </section>

  <section class="card card-back">
    <div class="back-brand">
      <span class="brand-mark"></span>
      <span class="brand-name">4 Ridges Real Estate</span>
    </div>
    <div class="tagline">
      <span class="tagline-rule"></span>
      <span>Raise Your Standards.</span>
      <span class="tagline-rule"></span>
    </div>
  </section>
</body>
</html>
```